Whiskerloft Flyer

Require a flyer for our pet photography business. I have uploaded a very poor attempt I have made at designing one. the size is to be DL and to be one page, but coloured on both sides. I have included the template to which the design is to fit.

Target Market(s)

Pet owners

Font styles to use
Sans Serif

Requirements
Must have
• I have included snap shots from our webdesign. The flyer design should be complimentary to the web design. Please use wording on the flyer front from the files called webscreenshots
Nice to have
• The back: a portfolio of the images on the back side with the logo and the website.
• The front: On the front side we would like a maximum of three photos (different to the ones used on the back) with the writing from the screen shots and the logo.
• check the names of the photos to be put on the flyer, I have called them back and front as appropriate.

```html
<!DOCTYPE html>
<html lang="en">
<head>
<meta charset="utf-8">
<title>Whiskerloft Flyer</title>
<link rel="stylesheet" href="https://fonts.googleapis.com/css2?family=Roboto+Condensed:wght@300;400;700;900&family=Roboto:wght@300;400;500;700&display=swap">
<style>
  :root{
    --coral:#ef5a5c;
    --ink:#3b3b3b;
    --ink-soft:#6d6d6d;
    --paper:#ffffff;
    --canvas:#ececec;
    --footer:#bdbdc0;
    --frame:#2a2a2a;
    --brand:#d8262c;
  }
  *{box-sizing:border-box;margin:0;padding:0}
  html,body{width:800px;height:1200px;overflow:hidden;background:var(--canvas)}
  body{position:relative;font-family:"Roboto",Arial,sans-serif;color:var(--ink)}
  .flyer{position:absolute;top:220px;width:360px;height:760px;background:var(--paper);overflow:hidden;box-shadow:0 2px 10px rgba(0,0,0,.12)}
  .flyer--front{left:30px}
  .flyer--back{left:410px}
  .abs{position:absolute}

  .hero{position:absolute;left:0;top:0}
  .headline{position:absolute;left:9px;top:78px;width:148px;font-family:"Roboto Condensed",Arial,sans-serif;font-weight:400;color:var(--paper);line-height:1.08}
  .headline__line{font-size:22px;display:block}
  .headline__amp{position:absolute;left:104px;top:-4px;font-size:54px;font-weight:400;line-height:1}
  .headline__sub{font-size:19px;display:block;margin-top:3px}
  .headline__avail{font-size:18.5px;font-weight:300;color:#ffe1e1;display:block;margin-top:8px}
  .headline__place{font-size:37px;font-weight:900;color:var(--ink);display:block;letter-spacing:-1px;margin-top:1px;white-space:nowrap}

  .ease{left:10px;top:337px}
  .ease__title{font-size:25px;font-weight:500;color:var(--ink-soft);letter-spacing:.5px}
  .ease__sub{font-size:9.5px;font-weight:500;color:var(--ink-soft);margin-top:2px}
  .ease__copy{left:183px;top:339px;width:165px;font-size:8.5px;line-height:1.3;color:var(--ink-soft);text-align:justify}

  .shot{position:absolute;top:435px;height:108px}
  .shot--left{left:11px;width:169px;border-top-right-radius:26px;
    background:radial-gradient(ellipse 38% 30% at 52% 52%,#f1e6d6 0%,#c98a4e 45%,rgba(120,70,30,.6) 75%,transparent 100%),#050403}
  .shot--right{left:186px;width:161px;border-top-left-radius:26px;
    background:radial-gradient(ellipse 45% 38% at 55% 50%,#eeeae4 0%,#b9b1a6 40%,rgba(90,85,80,.55) 72%,transparent 100%),#050505}

  .badge{left:11px;top:566px;width:76px;height:76px;border-radius:50%;border:2px solid #d7d7d7;background:var(--paper)}
  .team{left:10px;top:651px;font-size:10px;font-weight:500;color:var(--ink);line-height:1.35}
  .team__names{font-size:14px;font-weight:700;color:var(--ink-soft);line-height:1.3;margin-top:2px}

  .getall{left:183px;top:566px;width:165px}
  .getall__title{font-size:14px;font-weight:500;color:var(--ink)}
  .getall__copy{font-size:9.5px;color:var(--ink-soft);line-height:1.3;margin-top:4px}

  .brand{display:flex;flex-direction:column;align-items:center;gap:3px}
  .brand__dot{width:18px;height:18px;border-radius:50%;border:1.5px solid var(--brand)}
  .brand__name{font-family:"Roboto Condensed",Arial,sans-serif;font-size:11px;font-weight:700;color:var(--brand);letter-spacing:.5px}
  .brand--front{left:240px;top:674px;width:100px}
  .brand--back{left:130px;top:16px;width:100px}

  .footer{position:absolute;left:0;bottom:0}
  .footer__phone{left:10px;bottom:10px;font-size:8px;font-weight:700;color:var(--ink);display:flex;align-items:center;gap:6px}
  .footer__contact{left:183px;bottom:5px;font-size:7.5px;font-weight:700;color:var(--ink);line-height:1.5}
  .footer__row{display:flex;align-items:center;gap:8px}

  .tile{position:absolute;border:2px solid var(--frame);box-shadow:2px 3px 4px rgba(0,0,0,.35)}
  .tile--horse{left:11px;top:61px;width:336px;height:132px;
    background:radial-gradient(ellipse 30% 55% at 72% 45%,#f3e2c4 0%,rgba(214,170,110,.7) 50%,transparent 100%),
               radial-gradient(ellipse 40% 70% at 25% 70%,#7a3c1c 0%,#4a2412 60%,transparent 100%),
               linear-gradient(180deg,#dfe6ee 0%,#c9d2dc 55%,#8a7b6a 100%)}
  .tile--shaggy{left:11px;top:199px;width:156px;height:162px;
    background:radial-gradient(ellipse 40% 42% at 50% 45%,#f6efe4 0%,#d9c9b0 45%,rgba(120,85,55,.6) 75%,transparent 100%),#3e2a1c}
  .tile--mastiff{left:174px;top:199px;width:173px;height:107px;
    background:radial-gradient(ellipse 38% 60% at 50% 55%,#b98456 0%,#8a5a36 45%,rgba(160,130,100,.5) 75%,transparent 100%),linear-gradient(180deg,#e3d7c6,#c9b69c)}
  .tile--collie{left:174px;top:311px;width:173px;height:151px;
    background:radial-gradient(ellipse 30% 40% at 28% 45%,#1c1c1c 0%,#2e2e2e 50%,transparent 100%),
               radial-gradient(ellipse 30% 45% at 72% 45%,#ead2bf 0%,#c7b9c6 50%,transparent 100%),
               linear-gradient(180deg,#6d7a55,#9da47e 55%,#3e4a5c 100%)}
  .tile--cathold{left:11px;top:364px;width:156px;height:151px;
    background:radial-gradient(ellipse 35% 30% at 50% 35%,#e8b99a 0%,#b5553a 55%,transparent 100%),
               radial-gradient(ellipse 50% 35% at 50% 85%,#f4f2ee 0%,#8c8c8c 60%,transparent 100%),linear-gradient(160deg,#dcc6ac,#c8a98b)}
  .tile--tabby{left:174px;top:467px;width:173px;height:151px;
    background:radial-gradient(ellipse 38% 45% at 50% 58%,#f1efec 0%,#9a8c7c 50%,rgba(90,65,45,.6) 78%,transparent 100%),linear-gradient(180deg,#3a2a1e,#6a4b32)}
  .tile--sharpei{left:11px;top:520px;width:156px;height:98px;
    background:radial-gradient(ellipse 35% 55% at 40% 55%,#d3a172 0%,#a87448 50%,rgba(70,50,35,.6) 80%,transparent 100%),#2b211a}
  .tile--poodle{left:11px;top:622px;width:336px;height:132px;
    background:radial-gradient(ellipse 14% 40% at 42% 55%,#fbf7f4 0%,#f3dcd6 60%,transparent 100%),
               radial-gradient(ellipse 10% 22% at 33% 70%,#f19bb4 0%,transparent 100%),
               radial-gradient(ellipse 10% 22% at 51% 70%,#f19bb4 0%,transparent 100%),#f0cfc6}
</style>
</head>
<body>

<section class="flyer flyer--front" aria-label="Flyer front">
  <svg class="hero" width="360" height="330" viewBox="0 0 360 330">
    <defs>
      <radialGradient id="heroFur" cx="0.55" cy="0.62" r="0.5">
        <stop offset="0" stop-color="#fbf8f1"/>
        <stop offset="0.45" stop-color="#ebe3d3"/>
        <stop offset="1" stop-color="#ebe3d3" stop-opacity="0"/>
      </radialGradient>
      <radialGradient id="heroHat" cx="0.55" cy="0.12" r="0.4">
        <stop offset="0" stop-color="#8e8c88"/>
        <stop offset="0.6" stop-color="#a9a7a3"/>
        <stop offset="1" stop-color="#a9a7a3" stop-opacity="0"/>
      </radialGradient>
      <linearGradient id="heroBg" x1="0" y1="0" x2="0" y2="1">
        <stop offset="0" stop-color="#d6dce3"/>
        <stop offset="1" stop-color="#c3cbd4"/>
      </linearGradient>
    </defs>
    <polygon points="0,0 360,0 360,262 0,327" fill="var(--coral)"/>
    <g role="img" aria-label="Photo of a fluffy white dog wearing a grey knitted hat">
      <polygon points="155,0 360,0 360,252 155,289" fill="url(#heroBg)"/>
      <polygon points="155,0 360,0 360,252 155,289" fill="url(#heroHat)"/>
      <polygon points="155,0 360,0 360,252 155,289" fill="url(#heroFur)"/>
    </g>
  </svg>
  <h1 class="headline">
    <span class="headline__line">Fun quirky</span>
    <span class="headline__line">beautiful</span>
    <span class="headline__amp">&amp;</span>
    <span class="headline__sub">pet photography</span>
    <span class="headline__avail">Now available in</span>
    <span class="headline__place">MARLOW</span>
  </h1>

  <div class="abs ease">
    <h2 class="ease__title">Be At Ease</h2>
    <p class="ease__sub">In Studio| On Location| At Home</p>
  </div>
  <p class="abs ease__copy">All session are available to ensure you and your pet are comfortable (Note: At this time all Whiskerloft Pet Photography is only available in studio)</p>

  <div class="shot shot--left" role="img" aria-label="Photo of a beagle leaping against a black background"></div>
  <div class="shot shot--right" role="img" aria-label="Photo of a fluffy cat rolling on its back against a black background"></div>

  <div class="abs badge" role="img" aria-label="Professional accreditation badge"></div>
  <div class="abs getall">
    <h3 class="getall__title">You Get it All!</h3>
    <p class="getall__copy">Beautifully printed photographs on art paper along with the digital files.</p>
  </div>
  <div class="abs team">
    <p>Award Winning Pet Loving<br>Photographers</p>
    <p class="team__names">Daniel Pryce &amp;<br>Carol Emberly</p>
  </div>
  <div class="abs brand brand--front">
    <span class="brand__dot"></span>
    <span class="brand__name">WHISKERLOFT</span>
  </div>

  <svg class="footer" width="360" height="32" viewBox="0 0 360 32">
    <polygon points="0,10 360,0 360,32 0,32" fill="var(--footer)"/>
  </svg>
  <div class="abs footer__phone">
    <svg width="9" height="9" viewBox="0 0 24 24"><path d="M6.6 10.8a15.1 15.1 0 006.6 6.6l2.2-2.2c.3-.3.7-.4 1-.2 1.1.4 2.3.6 3.6.6.6 0 1 .4 1 1V20c0 .6-.4 1-1 1A17 17 0 013 4c0-.6.4-1 1-1h3.5c.6 0 1 .4 1 1 0 1.3.2 2.5.6 3.6.1.3 0 .7-.2 1z" fill="var(--ink)"/></svg>
    <span>Carol 0412 555 318</span>
  </div>
  <div class="abs footer__contact">
    <p class="footer__row"><svg width="9" height="7" viewBox="0 0 24 18"><rect width="24" height="18" rx="2" fill="var(--ink)"/><path d="M2 2l10 8 10-8" stroke="#fff" stroke-width="2" fill="none"/></svg>hello@whiskerloftpets.com</p>
    <p class="footer__row"><svg width="9" height="9" viewBox="0 0 24 24"><circle cx="12" cy="12" r="11" fill="var(--ink)"/><path d="M1 12h22M12 1c4 4 4 18 0 22M12 1c-4 4-4 18 0 22" stroke="#fff" stroke-width="1.5" fill="none"/></svg>www.whiskerloftpets.com</p>
  </div>
</section>

<section class="flyer flyer--back" aria-label="Flyer back">
  <div class="abs brand brand--back">
    <span class="brand__dot"></span>
    <span class="brand__name">WHISKERLOFT</span>
  </div>

  <div class="tile tile--horse" role="img" aria-label="Photo of a woman kissing a brown horse"></div>
  <div class="tile tile--shaggy" role="img" aria-label="Photo of a small shaggy dog"></div>
  <div class="tile tile--mastiff" role="img" aria-label="Photo of a bullmastiff"></div>
  <div class="tile tile--collie" role="img" aria-label="Photo of a woman sitting with a border collie"></div>
  <div class="tile tile--cathold" role="img" aria-label="Photo of a woman holding a grey cat"></div>
  <div class="tile tile--tabby" role="img" aria-label="Photo of a tabby and white cat"></div>
  <div class="tile tile--sharpei" role="img" aria-label="Photo of a shar pei"></div>
  <div class="tile tile--poodle" role="img" aria-label="Photo of a white poodle with pink flowers"></div>
</section>

</body>
</html>
```